Luxury Brand Real Estate For Sale sign

**Update** I've added some examples from the internet of other signs that have a look similar to what I would like to see. I do not want my personal name in the sign. And the word FOR SALE Does not need to be so large - it can be more subtle.
I want to create a Real Estate for sale sign for my company that will be used for luxury/higher end real estate listings. I’m sharing my business card as well as a logo with new teal color to show what we're moving towards: we’re using Teal, white, black and gold.
Hoping the sign is simple, sophisticated and eye catching.
The sign should be 24" wide by 30" tall including the company name: Harbor Crest Realty Group and our logo, office phone number 727-555-0148 and website www.hcrgexample.com the words "For Sale"
Optional to add this e-mail address info@hcrgexample.com to the sign
Target Market(s)
Luxury home buyers
Industry/Entity Type
Real Estate
Look and feel

```html
<!DOCTYPE html>
<html lang="en">
<head>
<meta charset="utf-8">
<title>Harbor Crest Realty Group — For Sale Sign</title>
<link rel="stylesheet" href="https://fonts.googleapis.com/css2?family=Montserrat:wght@700&family=Questrial&display=swap">
<style>
  :root {
    --ink: #19191b;
    --teal: #2b8378;
    --silver: #c0c4c7;
  }
  * { margin: 0; padding: 0; box-sizing: border-box; }
  html, body {
    width: 1200px;
    height: 1200px;
    overflow: hidden;
    background: var(--ink);
  }
  .sign {
    position: absolute;
    left: 0;
    width: 1200px;
    height: 600px;
    font-family: "Questrial", sans-serif;
  }
  .sign--dark { top: 0; background: var(--ink); --accent: var(--teal); --detail: var(--silver); }
  .sign--teal { top: 600px; background: var(--teal); --accent: var(--silver); --detail: var(--ink); }

  .sign__frame {
    position: absolute;
    left: 137px;
    top: 61px;
    width: 926px;
    height: 478px;
    border: 13px solid var(--silver);
  }
  .brand-mark {
    position: absolute;
    left: 198px;
    top: 150px;
    display: flex;
    align-items: center;
    gap: 18px;
    color: var(--accent);
  }
  .brand-mark__square {
    width: 22px;
    height: 22px;
    background: var(--accent);
  }
  .brand-mark__name {
    font-size: 92px;
    line-height: 1;
    letter-spacing: 4px;
  }
  .sign__divider {
    position: absolute;
    left: 549px;
    top: 109px;
    width: 5px;
    height: 171px;
    background: var(--accent);
  }
  .company-name {
    position: absolute;
    left: 609px;
    top: 150px;
    color: var(--accent);
    font-size: 40px;
    line-height: 48px;
    text-transform: uppercase;
    letter-spacing: 0.5px;
  }
  .sale-block {
    position: absolute;
    right: 193px;
    top: 312px;
    text-align: right;
    color: var(--detail);
  }
  .sale-block__headline {
    font-family: "Montserrat", sans-serif;
    font-weight: 700;
    font-size: 95px;
    line-height: 100px;
    letter-spacing: -1px;
    color: var(--silver);
  }
  .sign--teal .sale-block__headline { color: var(--ink); }
  .contact-line {
    white-space: nowrap;
    font-size: 27px;
    line-height: 1;
  }
  .contact-line--phone { margin-top: 12px; }
  .contact-line--web { margin-top: 12px; }
  .contact-line__value--phone {
    font-size: 35px;
    margin-left: 20px;
    letter-spacing: 0.5px;
  }
</style>
</head>
<body>
  <section class="sign sign--dark" aria-label="For sale sign, dark version">
    <div class="sign__frame"></div>
    <div class="brand-mark"><span class="brand-mark__square"></span><span class="brand-mark__name">HCRG</span></div>
    <div class="sign__divider"></div>
    <p class="company-name">Harbor Crest<br>Realty Group</p>
    <div class="sale-block">
      <h1 class="sale-block__headline">FOR SALE</h1>
      <p class="contact-line contact-line--phone">phone number<span class="contact-line__value--phone">727-555-0148</span></p>
      <p class="contact-line contact-line--web">website www.hcrgexample.com</p>
    </div>
  </section>

  <section class="sign sign--teal" aria-label="For sale sign, teal version">
    <div class="sign__frame"></div>
    <div class="brand-mark"><span class="brand-mark__square"></span><span class="brand-mark__name">HCRG</span></div>
    <div class="sign__divider"></div>
    <p class="company-name">Harbor Crest<br>Realty Group</p>
    <div class="sale-block">
      <h2 class="sale-block__headline">FOR SALE</h2>
      <p class="contact-line contact-line--phone">phone number<span class="contact-line__value--phone">727-555-0148</span></p>
      <p class="contact-line contact-line--web">website www.hcrgexample.com</p>
    </div>
  </section>
</body>
</html>
```